Eyeglass Lens company needs packaging design for small shipping box

We are eye doctors with a lab to replace eyeglass lenses at an affordable price called OptiBrim. We are a new company based in Southern California. We replace old prescription lenses with new ones in patients own frame. About 50% of jobs could take only 1-2 days to make and send back. Patients select the lenses and give us the prescription. We then send a box with a prepaid shipping label. Place the frames in the box and drop them in the mail to our lab. We will custom make new lenses, fit them back into your frames and send them back to you. We would like to compete with www.vuecraft-demo.com and offer affordable lenses for single vision, bifocal, progressive, sunglass lenses at an affordable price with fast shipping.

Attached is the website design templete to get an idea of our website.
Updates

Update: I uploaded pictures of the logo. The slight issue I have with the logo is it's similar to a competitor. If there is a way to tweak the logo that would be great and a huge plus.. Otherwise, if not, it's fine to leave the way it is. Thank You

Update: Hi, I'm looking for a simple design that is somewhat professional but can also fun, cute. We are eye doctors and want to relay a level of professionalism. Black box with logo and cute eyelash designs (like the eyelash pillow picture). Also, look at the sample box I'd like to model and improve. Go to vuecraft-demo.com or glintmora-demo.com for simple looks as an example.

Target Market(s)

20-65 yo male/female wears glasses, has children or family members that wear glasses. Coupon hunters, discount retailers, online shopping

Industry/Entity Type

Eyewear

Colors
000000
9bcb3b
ffffff

Requirements
Must have
• Must be neutral for both genders but cute is a plus.
• Attached is a sample box of the exact size and type of shipping box.
• The shipping box will contain the eyeglass frames. We ship box, patient puts frame in box, sends the box to us, we replace prescription lenses in frame, send back to patient.
• The dimensions of the shipping box are 7 7/8" Length x 3 3/8" Width x 2 1/4" Height
• I would like see the box black/dark grey or I'm open to other designs as well. This is creative open project.
• There is a picture uploaded that has instructions on how they should put the frame in the box. Please recreate something similar but different inside the box giving instructions.
• Make room for the shipping label on one or two sides of the box!
Nice to have
• Cute, cool, simple fun designs. Designs on the side of the box and inside the box.
• I'm trying to simplify a complicated process with doctors, prescriptions, insurance.
• So a simplified first impression is best.
• Eyelashes are cute

```html
<!DOCTYPE html>
<html lang="en">
<head>
<meta charset="utf-8">
<title>OptiBrim – Shipping Box Panels</title>
<link rel="stylesheet" href="https://fonts.googleapis.com/css2?family=Questrial&family=Mulish:wght@700&display=swap">
<style>
  :root {
    --brand-black: #000000;
    --brand-green: #8dc63f;
    --brand-white: #ffffff;
    --page-bg: #ffffff;
    --text-font: "Questrial", sans-serif;
    --tagline-font: "Mulish", sans-serif;
  }
  * { margin: 0; padding: 0; box-sizing: border-box; }
  html, body {
    width: 1200px; height: 1200px; overflow: hidden;
    background: var(--page-bg);
  }
  .canvas { position: relative; width: 1200px; height: 1200px; }

  .panel { position: absolute; background: var(--brand-black); overflow: hidden; }

  /* Lid / front panel */
  .panel--lid { left: 100px; top: 378px; width: 578px; height: 247px; }
  .lid__brand {
    position: absolute; right: 26px; top: 62px;
    font-family: var(--text-font); font-size: 52px; line-height: 1;
    color: var(--brand-white); letter-spacing: 0.5px;
  }
  .lid__tagline {
    position: absolute; left: 22px; top: 176px;
    font-family: var(--tagline-font); font-weight: 700; font-size: 24px;
    color: var(--brand-white);
  }
  .lid__url-bar {
    position: absolute; left: 246px; top: 176px; width: 332px; height: 33px;
    background: var(--brand-green);
    display: flex; align-items: center; justify-content: center;
    font-family: var(--text-font); font-size: 20px; color: var(--brand-black);
  }

  /* Side panel */
  .panel--side { left: 100px; top: 657px; width: 578px; height: 164px; }
  .side__url {
    position: absolute; left: 0; right: 0; top: 70px; text-align: center;
    font-family: var(--text-font); font-size: 20px; color: var(--brand-green);
  }
  .side__band {
    position: absolute; left: 0; right: 0; bottom: 0; height: 13px;
    background: var(--brand-green);
  }

  /* End flap / instructions */
  .panel--steps { left: 730px; top: 585px; width: 356px; height: 236px; }
  .steps__stripe {
    position: absolute; left: 56px; top: 0; width: 48px; height: 100%;
    background: var(--brand-green);
  }
  .steps__brand-block {
    position: absolute; left: 26px; top: 15px; width: 110px; height: 66px;
    background: var(--brand-black);
    display: flex; flex-direction: column; align-items: center; justify-content: center; gap: 6px;
  }
  .steps__brand-dot {
    width: 30px; height: 30px; border-radius: 50%;
    border: 1.5px solid var(--brand-green);
  }
  .steps__brand {
    font-family: var(--text-font); font-size: 17px; line-height: 1;
    color: var(--brand-white);
  }
  .steps__list {
    position: absolute; left: 114px; top: 88px; list-style: none;
    font-family: var(--text-font); font-size: 16px; line-height: 23px;
    color: var(--brand-green);
  }
  .steps__item { display: flex; gap: 8px; }
  .steps__tick { flex: none; width: 12px; height: 12px; margin-top: 6px; }
</style>
</head>
<body>
<main class="canvas">

  <section class="panel panel--lid">
    <div class="lid__brand">OptiBrim</div>
    <p class="lid__tagline">Let’s get started.</p>
    <div class="lid__url-bar">www.vuecraft-demo.com</div>
  </section>

  <section class="panel panel--side">
    <p class="side__url">www.vuecraft-demo.com</p>
    <div class="side__band"></div>
  </section>

  <section class="panel panel--steps">
    <div class="steps__stripe"></div>
    <div class="steps__brand-block">
      <span class="steps__brand-dot"></span>
      <span class="steps__brand">OptiBrim</span>
    </div>
    <ul class="steps__list">
      <li class="steps__item"><svg class="steps__tick" viewBox="0 0 12 12"><circle cx="6" cy="6" r="5" fill="none" stroke="#8dc63f" stroke-width="1.4"/><path d="M3.5 6.2l1.8 1.7 3.2-3.4" fill="none" stroke="#8dc63f" stroke-width="1.4"/></svg><span>We ship box</span></li>
      <li class="steps__item"><svg class="steps__tick" viewBox="0 0 12 12"><circle cx="6" cy="6" r="5" fill="none" stroke="#8dc63f" stroke-width="1.4"/><path d="M3.5 6.2l1.8 1.7 3.2-3.4" fill="none" stroke="#8dc63f" stroke-width="1.4"/></svg><span>Patient puts frame in box</span></li>
      <li class="steps__item"><svg class="steps__tick" viewBox="0 0 12 12"><circle cx="6" cy="6" r="5" fill="none" stroke="#8dc63f" stroke-width="1.4"/><path d="M3.5 6.2l1.8 1.7 3.2-3.4" fill="none" stroke="#8dc63f" stroke-width="1.4"/></svg><span>Sends the box to us</span></li>
      <li class="steps__item"><svg class="steps__tick" viewBox="0 0 12 12"><circle cx="6" cy="6" r="5" fill="none" stroke="#8dc63f" stroke-width="1.4"/><path d="M3.5 6.2l1.8 1.7 3.2-3.4" fill="none" stroke="#8dc63f" stroke-width="1.4"/></svg><span>We replace prescription<br>lenses in frame</span></li>
      <li class="steps__item"><svg class="steps__tick" viewBox="0 0 12 12"><circle cx="6" cy="6" r="5" fill="none" stroke="#8dc63f" stroke-width="1.4"/><path d="M3.5 6.2l1.8 1.7 3.2-3.4" fill="none" stroke="#8dc63f" stroke-width="1.4"/></svg><span>Send back to patient</span></li>
    </ul>
  </section>

</main>
</body>
</html>
```